Business Card Design Project for Female Personal Trainer

I need a business card design to appeal to female clients for my personal training and group fitness boot camp business called 'Lumeva Studios'. It should be girly, fun and have an active/healthy pic or figure incorporated into the business name.

Target Market(s)

- Females 20-65yrs

Industry/Entity Type

Training

Font styles to use
Serif
Sans Serif

Colors
e34197
e567a6

Requirements
Must have
• First Side of Business Card Details :

Corin Delph
MASTER PERSONAL TRAINER
Cert III & Cert IV in Fitness
Senior First Aid
Mobile: 0438 507 164
Email: lumeva@quillpost.net
Facebook: Lumeva Studios

* Mobile Personal Training *Individual Sessions *Bootcamp *Weight-loss and Toning

Second Side of Business Card I want to offer a free personal consult:
Something like this:

Need direction with your health & fitness goals?

Call now for your free 1 on 1 Personal Training Session with full consultation

Nice to have
• Have a sub-heading for example:

'Promoting healthy living through fitness & nutrition'

- have the colour pink or blue (to appeal to a female)

- a picture/motif//logo attached (sometimes a picture paints a thousand words)

Should not have
• * picture of a person with big muscles or appeal to a man (I'm training women only)

* should not be busy or crammed up look (if I've added to much info above please just use to your discretion).

```html
<!DOCTYPE html>
<html lang="en">
<head>
<meta charset="utf-8">
<title>Lumeva Studios – Business Card</title>
<link href="https://fonts.googleapis.com/css2?family=Marcellus+SC&family=Arimo:wght@400;700&family=Bebas+Neue&display=swap" rel="stylesheet">
<style>
  :root {
    --pink: #e34197;
    --pink-soft: #e567a6;
    --pink-pale: #f2a9cd;
    --white: #ffffff;
    --ink: #444448;
    --backdrop: #e4e4e6;
    --figure-light: #f0f0f0;
    --figure-dark: #d8d8d8;
  }
  * { box-sizing: border-box; margin: 0; padding: 0; }
  html, body { width: 1200px; height: 800px; overflow: hidden; }
  body {
    background: var(--backdrop);
    font-family: "Arimo", Arial, sans-serif;
    position: relative;
  }
  .card {
    position: absolute;
    width: 520px;
    height: 318px;
    top: 241px;
    overflow: hidden;
    box-shadow: 0 4px 14px rgba(0,0,0,0.12);
  }
  /* Back side */
  .card-back {
    left: 60px;
    background: var(--pink);
    color: var(--white);
    text-align: center;
    padding: 0 20px;
  }
  .offer-heading {
    font-family: "Bebas Neue", "Arial Narrow", sans-serif;
    font-weight: 400;
    font-size: 25px;
    letter-spacing: 0.3px;
    margin-top: 48px;
  }
  .offer-line {
    font-size: 12px;
    margin-top: 6px;
  }
  .program-icon {
    width: 64px;
    height: 64px;
    margin: 32px auto 10px;
    border-radius: 50%;
    background: var(--white);
    display: flex;
    align-items: center;
    justify-content: center;
  }
  .program-title {
    font-weight: 700;
    font-size: 13px;
    margin-bottom: 6px;
  }
  .program-list {
    font-size: 13px;
    line-height: 1.4;
  }
  /* Front side */
  .card-front {
    left: 620px;
    background: var(--white);
  }
  .figure-area {
    position: absolute;
    left: 412px;
    top: 92px;
    width: 78px;
    height: 165px;
    border-radius: 36px 36px 10px 10px;
    background: linear-gradient(180deg, var(--figure-dark), var(--figure-light));
  }
  .card-front .wave {
    position: absolute;
    inset: 0;
  }
  .identity {
    position: absolute;
    left: 34px;
    top: 30px;
    color: var(--ink);
  }
  .name {
    font-family: "Marcellus SC", Georgia, serif;
    font-weight: 400;
    color: var(--pink);
    font-size: 30px;
    line-height: 1;
    margin-bottom: 8px;
  }
  .credentials {
    font-size: 11px;
    line-height: 1.3;
  }
  .credentials .role { text-transform: uppercase; }
  .contacts {
    list-style: none;
    margin-top: 12px;
    font-size: 11px;
    line-height: 1.4;
  }
  .contacts li { display: flex; align-items: center; gap: 8px; }
  .contact-icon { width: 10px; height: 10px; flex: none; }
  .services {
    position: absolute;
    left: 20px;
    top: 250px;
    width: 380px;
    text-align: center;
    color: var(--white);
    font-size: 11px;
    line-height: 1.5;
  }
</style>
</head>
<body>

  <section class="card card-back" aria-label="Business card, back">
    <h2 class="offer-heading">Need direction with your health &amp; fitness goals?</h2>
    <p class="offer-line">Call now for your free 1 on 1 Personal Training Session with full consultation</p>
    <div class="program-icon">
      <svg width="36" height="20" viewBox="0 0 36 20" aria-hidden="true">
        <g fill="var(--pink)">
          <rect x="2" y="6" width="3" height="8" rx="1"/>
          <rect x="6" y="2" width="4" height="16" rx="1"/>
          <rect x="10" y="9" width="16" height="2"/>
          <rect x="26" y="2" width="4" height="16" rx="1"/>
          <rect x="31" y="6" width="3" height="8" rx="1"/>
        </g>
      </svg>
    </div>
    <p class="program-title">Fitness Programs</p>
    <p class="program-list">Weight loss consults • female specific training<br>body sculpting • HIIT • pre-post natal</p>
  </section>

  <section class="card card-front" aria-label="Business card, front">
    <div class="figure-area" role="img" aria-label="Soft grey silhouette of a woman in an active pose"></div>
    <svg class="wave" width="520" height="318" viewBox="0 0 520 318" aria-hidden="true">
      <path d="M0,178 C150,180 330,222 520,240 L520,248 C330,232 150,192 0,190 Z" fill="var(--pink-pale)"/>
      <path d="M0,196 C160,204 330,240 520,254 L520,262 C490,290 460,318 430,318 L0,318 Z" fill="var(--pink)"/>
      <path d="M0,196 C160,204 330,240 520,254 L520,262 C330,250 160,212 0,206 Z" fill="var(--pink-soft)"/>
    </svg>

    <div class="identity">
      <h1 class="name">Corin Delph</h1>
      <p class="credentials"><span class="role">Master Personal Trainer</span><br>Cert III &amp; Cert IV in Fitness<br>Senior First Aid</p>
      <ul class="contacts">
        <li>
          <svg class="contact-icon" viewBox="0 0 10 10" aria-hidden="true"><rect x="2" y="0" width="6" height="10" rx="1.2" fill="var(--pink)"/><rect x="3" y="1.5" width="4" height="6" fill="var(--white)"/></svg>
          0438 507 164
        </li>
        <li>
          <svg class="contact-icon" viewBox="0 0 10 10" aria-hidden="true"><rect x="0" y="2" width="10" height="7" fill="var(--pink)"/><path d="M0.5,2.5 L5,6 L9.5,2.5" stroke="var(--white)" fill="none"/></svg>
          lumeva@quillpost.net
        </li>
        <li>
          <svg class="contact-icon" viewBox="0 0 10 10" aria-hidden="true"><rect x="1" y="1" width="8" height="8" fill="var(--pink)"/></svg>
          Lumeva Studios
        </li>
      </ul>
    </div>

    <p class="services">Mobile Personal Training • Group Sessions • Individual Sessions<br>Bootcamp • Boxing for strength and fitness • Weight-loss and Toning<br>General Fitness</p>
  </section>

</body>
</html>
```